CloudRiver Business Card

I need something that flows with the logo and looks professional but creative. I included the thumbnail file of the photo but will upload the source file once I have it. Colors of business card should flow. I am interested in doing the translucent clear plastic cards as well. My company is called CloudRiver in one word and the contact details are below:

Dale Hollings
555-318-4720
www.CloudRiverTx.example
dhollings_47@mailbox.example
Updates

Too much red. I'd rather focus on the blue and put some silver or grey in there.

New Files uploaded. Like the designs so far and am looking forward to seeing more.

Looking for a whole new direction. Let's forget about the plastic card. Let's focus on the blue more than red. I still haven't seen something that really grabs me.

Industry/Entity Type

Plastic

```html
<!DOCTYPE html>
<html lang="en">
<head>
<meta charset="UTF-8">
<title>CloudRiver Business Card</title>
<link rel="stylesheet" href="https://fonts.googleapis.com/css2?family=Exo+2:wght@400;600;800&display=swap">
<style>
  :root {
    --page-bg: #e4e4e6;
    --card-black: #121214;
    --card-black-soft: #232327;
    --brand-red: #d2203c;
    --brand-purple: #3d2c8f;
    --brand-blue: #4e95d6;
    --brand-blue-light: #7db6e6;
    --name-blue: #3d4f8c;
    --web-blue: #3f88cf;
    --text-white: #f4f7fb;
  }
  * { margin: 0; padding: 0; box-sizing: border-box; }
  html, body {
    width: 1200px; height: 750px; overflow: hidden;
    background: var(--page-bg);
    font-family: "Exo 2", sans-serif;
  }
  .canvas {
    position: relative; width: 1200px; height: 750px;
  }
  .card {
    position: absolute; top: 235px;
    width: 500px; height: 280px;
    border-radius: 26px; overflow: hidden;
    background: linear-gradient(160deg, var(--card-black-soft), var(--card-black) 55%);
    box-shadow: 0 10px 24px rgba(0,0,0,0.22);
  }
  .card-front { left: 70px; }
  .card-back { left: 630px; }

  .front-wordmark {
    position: absolute; left: 0; right: 0; top: 95px;
    text-align: center;
    font-size: 58px; font-weight: 800;
    color: var(--brand-red);
    letter-spacing: 1px;
  }
  .front-web {
    position: absolute; left: 0; right: 0; top: 178px;
    text-align: center;
    font-size: 22px; font-weight: 400;
    color: var(--web-blue);
  }

  .back-waves { position: absolute; inset: 0; width: 100%; height: 100%; }
  .back-wordmark {
    position: absolute; left: 32px; top: 88px;
    font-size: 44px; font-weight: 800;
    color: var(--brand-red);
  }
  .holder { position: absolute; left: 34px; top: 150px; color: var(--name-blue); }
  .holder-name { font-size: 17px; font-weight: 600; line-height: 1.1; }
  .holder-role { font-size: 15px; font-weight: 400; }
  .contact {
    position: absolute; display: flex; align-items: center; gap: 7px;
    color: var(--text-white); font-size: 15px; font-weight: 400;
  }
  .contact-phone { left: 34px; top: 240px; }
  .contact-email { left: 262px; top: 176px; font-size: 14px; }
  .contact-icon { width: 18px; height: 18px; flex: none; }
</style>
</head>
<body>
<main class="canvas">
  <section class="card card-front" aria-label="Business card front">
    <div class="front-wordmark">CloudRiver</div>
    <div class="front-web">www.CloudRiverTx.example</div>
  </section>

  <section class="card card-back" aria-label="Business card back">
    <svg class="back-waves" viewBox="0 0 500 280" preserveAspectRatio="none" aria-hidden="true">
      <defs>
        <linearGradient id="blueBand" x1="0" y1="1" x2="1" y2="0">
          <stop offset="0" stop-color="var(--brand-blue-light)"/>
          <stop offset="1" stop-color="var(--brand-blue)"/>
        </linearGradient>
        <linearGradient id="redStripe" x1="0" y1="0" x2="1" y2="0">
          <stop offset="0" stop-color="var(--brand-red)"/>
          <stop offset="0.75" stop-color="var(--brand-red)" stop-opacity="0.9"/>
          <stop offset="1" stop-color="var(--brand-red)" stop-opacity="0"/>
        </linearGradient>
      </defs>
      <path d="M0 200 C160 198 330 180 470 118 C350 190 160 218 0 224 Z" fill="url(#redStripe)"/>
      <path d="M0 222 C150 214 350 176 500 100 L500 122 C350 190 150 226 0 236 Z" fill="var(--brand-purple)"/>
      <path d="M0 234 C150 224 350 188 500 120 L500 280 L0 280 Z" fill="url(#blueBand)"/>
    </svg>

    <div class="back-wordmark">CloudRiver</div>
    <div class="holder">
      <div class="holder-name">Dale Hollings</div>
      <div class="holder-role">role</div>
    </div>

    <div class="contact contact-email">
      <svg class="contact-icon" viewBox="0 0 20 20" aria-hidden="true">
        <circle cx="10" cy="10" r="9" fill="var(--text-white)"/>
        <rect x="5" y="6.5" width="10" height="7" rx="1" fill="none" stroke="var(--brand-blue)" stroke-width="1.4"/>
        <path d="M5.5 7 L10 10.5 L14.5 7" fill="none" stroke="var(--brand-blue)" stroke-width="1.4"/>
      </svg>
      <span>dhollings_47@mailbox.example</span>
    </div>
    <div class="contact contact-phone">
      <svg class="contact-icon" viewBox="0 0 20 20" aria-hidden="true">
        <circle cx="10" cy="10" r="8.5" fill="none" stroke="var(--text-white)" stroke-width="1.4"/>
        <path d="M7 6 L8.5 6 L9.2 8.2 L8.2 9 C8.8 10.3 9.7 11.2 11 11.8 L11.8 10.8 L14 11.5 L14 13 C10 13.4 6.6 10 7 6 Z" fill="var(--text-white)"/>
      </svg>
      <span>555-318-4720</span>
    </div>
  </section>
</main>
</body>
</html>
```